Lakeshore Vision Associates, P.C.
Diseases and Surgeries of the Retina, Macula and Vitreous
Lakeshore Vision Associates, P.C. - Medical
Creative Brief
Professional
Peter R. Haldane, MD
Birchwood Medical Tower 4215 N. Lindon Suite 812 Wexmore, IL 60952
peter@lakeshorevsa.com
www.lakeshorevsa.com
Appointment Date: MM/DD/YYYY at ____________am ___________pm Please telephone in advance if you will be unable to keep the appointment

```html
<!DOCTYPE html>
<html lang="en">
<head>
<meta charset="utf-8">
<title>Lakeshore Vision Associates — Business Card</title>
<link href="https://fonts.googleapis.com/css2?family=EB+Garamond:wght@400;500&display=swap" rel="stylesheet">
<style>
  :root {
    --backdrop: #3a3a3a;
    --card: #ffffff;
    --ink: #2b2b2b;
    --ink-soft: #555555;
    --accent: #d2531f;
    --accent-deep: #b8421a;
    --steel: #9a9a9a;
    --steel-light: #d9d9d9;
    --rule: #bdbdbd;
  }
  html, body {
    margin: 0;
    width: 1200px;
    height: 780px;
    overflow: hidden;
    background: var(--backdrop);
    font-family: "EB Garamond", Georgia, serif;
  }
  .canvas {
    position: relative;
    width: 1200px;
    height: 780px;
  }
  .card {
    position: absolute;
    left: 75px;
    top: 90px;
    width: 1050px;
    height: 600px;
    background: var(--card);
    border-radius: 28px;
    overflow: hidden;
    box-shadow: 0 14px 40px rgba(0,0,0,0.45);
  }
  .card-edge {
    position: absolute;
    inset: 0;
  }
  .brand {
    position: absolute;
    left: 70px;
    top: 40px;
    display: flex;
    align-items: center;
    gap: 34px;
  }
  .brand-dot {
    width: 170px;
    height: 170px;
    border-radius: 50%;
    background: var(--accent);
  }
  .brand-name {
    margin: 0;
    width: 520px;
    font-size: 54px;
    font-weight: 500;
    line-height: 1.1;
    letter-spacing: 3px;
    text-transform: uppercase;
    color: var(--ink);
  }
  .person {
    position: absolute;
    right: 372px;
    top: 340px;
    text-align: right;
    color: var(--ink-soft);
  }
  .person-name {
    margin: 0;
    font-size: 44px;
    font-weight: 500;
    color: var(--accent);
    line-height: 1.1;
  }
  .person-title {
    margin: 0 0 26px;
    font-size: 26px;
  }
  .person-address {
    margin: 0;
    font-style: normal;
    font-size: 27px;
    line-height: 1.3;
    color: var(--ink);
  }
  .divider {
    position: absolute;
    left: 712px;
    top: 325px;
    width: 1px;
    height: 215px;
    background: var(--rule);
  }
  .contact {
    position: absolute;
    left: 735px;
    top: 322px;
    margin: 0;
    padding: 0;
    list-style: none;
    font-size: 27px;
    color: var(--ink);
  }
  .contact li {
    display: flex;
    align-items: center;
    gap: 14px;
    height: 54px;
  }
  .contact svg {
    width: 24px;
    height: 24px;
    flex: none;
  }
</style>
</head>
<body>
<main class="canvas">
  <section class="card">
    <svg class="card-edge" viewBox="0 0 1050 600" aria-hidden="true">
      <defs>
        <linearGradient id="steel" x1="0" y1="0" x2="1" y2="1">
          <stop offset="0" stop-color="var(--steel-light)"/>
          <stop offset="0.5" stop-color="var(--steel)"/>
          <stop offset="1" stop-color="var(--steel-light)"/>
        </linearGradient>
        <linearGradient id="band" x1="0" y1="0" x2="0" y2="1">
          <stop offset="0" stop-color="var(--accent)"/>
          <stop offset="1" stop-color="var(--accent-deep)"/>
        </linearGradient>
      </defs>
      <path d="M860 0 L915 0 C965 140 1005 320 1050 500 L1050 570 C1000 340 940 140 860 0 Z" fill="url(#steel)"/>
      <path d="M915 0 L1050 0 L1050 500 C1005 320 965 140 915 0 Z" fill="url(#band)"/>
    </svg>

    <header class="brand">
      <div class="brand-dot"></div>
      <h1 class="brand-name">Lakeshore Vision Associates</h1>
    </header>

    <div class="person">
      <p class="person-name">Peter R. Haldane, MD</p>
      <p class="person-title">President/CEO</p>
      <address class="person-address">Birchwood Medical Tower<br>4215 N. Lindon Suite 812, Wexmore, IL 60952</address>
    </div>

    <div class="divider"></div>

    <ul class="contact">
      <li>
        <svg viewBox="0 0 24 24"><path fill="var(--accent)" d="M6.6 10.8a15.1 15.1 0 0 0 6.6 6.6l2.2-2.2a1 1 0 0 1 1-.25 11.4 11.4 0 0 0 3.6.57 1 1 0 0 1 1 1V20a1 1 0 0 1-1 1A17 17 0 0 1 3 4a1 1 0 0 1 1-1h3.5a1 1 0 0 1 1 1c0 1.25.2 2.45.57 3.6a1 1 0 0 1-.25 1Z"/></svg>
        <span>(T) 555-318-4400</span>
      </li>
      <li>
        <svg viewBox="0 0 24 24"><path fill="var(--accent)" d="M7 3h10v5H7zM4 9h16a2 2 0 0 1 2 2v6h-4v4H6v-4H2v-6a2 2 0 0 1 2-2Zm4 7v3h8v-3Z"/></svg>
        <span>555-318-4426</span>
      </li>
      <li>
        <svg viewBox="0 0 24 24"><circle cx="12" cy="12" r="4" fill="none" stroke="var(--accent)" stroke-width="2.4"/><path d="M16 8v5.5a2.5 2.5 0 0 0 5 0V12a9 9 0 1 0-3.5 7.1" fill="none" stroke="var(--accent)" stroke-width="2.4"/></svg>
        <span>peter@lakeshorevsa.com</span>
      </li>
      <li>
        <svg viewBox="0 0 24 24"><g fill="none" stroke="var(--accent)" stroke-width="2"><circle cx="12" cy="12" r="9.5"/><ellipse cx="12" cy="12" rx="4" ry="9.5"/><path d="M2.5 12h19M4 7h16M4 17h16"/></g></svg>
        <span>www.lakeshorevsa.com</span>
      </li>
    </ul>
  </section>
</main>
</body>
</html>
```